Harborline Security and Surveillance Business Card

Business Card Design - Company Name:Freedom Security and SurveillanceWe are a Security Systems Integrator Specializing in Security Systems/ Video Surveillance and Access Control. Our areas of expertise are:Security SystemsVideo SurveillanceAccess ControlFire Alarm SystemsNetwork CablingCellular BoostersMy input is the Front of the Card is: logo, name of Business, My Name, Phone Number, and email.Rear of Card is the 6 areas of expertise, I just dont want the front to be very busy.
Name: Tom Werner
Title: President
Email: tom@harborlinesecsys.example
website: harborlinesecsys.example

```html
<!DOCTYPE html>
<html lang="en">
<head>
<meta charset="utf-8">
<title>Harborline Security and Surveillance – Business Card</title>
<link href="https://fonts.googleapis.com/css2?family=Saira:wght@500;600&family=Exo+2:wght@400;500&display=swap" rel="stylesheet">
<style>
  :root{
    --stage:#e9ebee;
    --blue:#2a7acb;
    --blue-deep:#1d5fae;
    --blue-light:#3a8ed8;
    --white:#ffffff;
    --paper:#f4f5f6;
    --grey-band:#c9ccd0;
    --grey-text:#8b8f94;
    --ink-blue:#2a6fc4;
  }
  *{box-sizing:border-box;margin:0;padding:0}
  html,body{width:1200px;height:780px;overflow:hidden;background:var(--stage)}
  .stage{width:1200px;height:780px;display:flex;align-items:center;justify-content:center;gap:40px}
  .card{width:540px;height:309px;position:relative;overflow:hidden;border-radius:3px;box-shadow:0 6px 18px rgba(0,0,0,.15)}

  /* Front */
  .card-front{background:var(--white);display:flex;flex-direction:column}
  .front-brand{height:150px;background:linear-gradient(180deg,var(--white),var(--paper));padding:48px 0 0 40px}
  .brand-name{font-family:"Saira",sans-serif;font-weight:600;font-size:38px;letter-spacing:2px;color:var(--ink-blue);line-height:1;text-transform:uppercase}
  .brand-sub{font-family:"Exo 2",sans-serif;font-size:13px;letter-spacing:13px;color:var(--grey-text);margin-top:8px;text-transform:uppercase}
  .front-role{height:30px;background:var(--grey-band);display:flex;align-items:center;padding-left:40px;font-family:"Exo 2",sans-serif;font-size:15px;text-transform:uppercase}
  .person-name{color:var(--ink-blue);letter-spacing:1px}
  .divider{width:1px;height:16px;background:var(--white);margin:0 12px}
  .person-title{color:var(--white);font-size:12px;letter-spacing:1px}
  .front-contact{flex:1;background:linear-gradient(160deg,var(--blue-light),var(--blue));padding:14px 40px;color:var(--white);font-family:"Exo 2",sans-serif;font-size:13.5px;line-height:1.45}
  .contact-line{display:flex;align-items:center;gap:8px}
  .contact-line svg{width:11px;height:11px;flex:none}

  /* Back */
  .card-back{background:linear-gradient(150deg,var(--blue-light),var(--blue-deep));color:var(--white);display:flex;flex-direction:column;align-items:center;justify-content:center}
  .back-texture{position:absolute;inset:0;background:radial-gradient(circle at 60% 40%,rgba(255,255,255,.08),rgba(0,0,0,.06))}
  .back-brand{position:relative;display:flex;align-items:center;gap:14px}
  .brand-dot{width:34px;height:34px;border-radius:50%;background:var(--white)}
  .back-brand .brand-name{color:var(--white);font-size:32px}
  .back-rule{position:relative;width:300px;height:1px;background:var(--white);margin:8px 0 6px}
  .back-sub{position:relative;font-family:"Exo 2",sans-serif;font-size:11px;letter-spacing:9px;text-transform:uppercase}
  .services{position:relative;margin-top:34px;font-family:"Exo 2",sans-serif;font-size:12.5px;text-align:center;line-height:1.7}
</style>
</head>
<body>
<main class="stage">
  <section class="card card-front">
    <div class="front-brand">
      <div class="brand-name">Harborline Security</div>
      <div class="brand-sub">and Surveillance</div>
    </div>
    <div class="front-role">
      <span class="person-name">Tom Werner</span>
      <span class="divider"></span>
      <span class="person-title">President</span>
    </div>
    <div class="front-contact">
      <div class="contact-line">Riverton Falls, Minnesota 56099</div>
      <div class="contact-line">United States</div>
      <div class="contact-line"><svg viewBox="0 0 11 11"><rect x="1" y="1" width="9" height="9" fill="none" stroke="#fff"/></svg>0100 555 0142</div>
      <div class="contact-line"><svg viewBox="0 0 11 11"><rect x="0.5" y="2" width="10" height="7" fill="none" stroke="#fff"/><path d="M0.5 2 L5.5 6 L10.5 2" fill="none" stroke="#fff"/></svg>tom@harborlinesecsys.example</div>
      <div class="contact-line"><svg viewBox="0 0 11 11"><circle cx="5.5" cy="5.5" r="4.8" fill="none" stroke="#fff"/><path d="M0.7 5.5h9.6M5.5 0.7v9.6" stroke="#fff" stroke-width=".8"/></svg>harborlinesecsys.example</div>
    </div>
  </section>

  <section class="card card-back">
    <div class="back-texture" role="img" aria-label="Faint repeating brand pattern across the blue background"></div>
    <div class="back-brand">
      <span class="brand-dot"></span>
      <span class="brand-name">Harborline Security</span>
    </div>
    <div class="back-rule"></div>
    <div class="back-sub">and Surveillance</div>
    <div class="services">
      Security Systems | Video Surveillance | Access Control | Fire Alarm Systems<br>
      Network Cabling | Cellular Boosters
    </div>
  </section>
</main>
</body>
</html>
```